Basic Company webpage with the elements and colors of our Logo

Basic Home page with a few pages:
- Home,
- About US,
- Contact us
- Services

Target Market(s)

Business Customers (B2B)

Coding

Coded - Design and coding required

Number of Pages Required

5+ page

Requirements
Must have
• Professional, Clean, Simple High Tech, Contact should have a contact us dialog for sending messages to us
Nice to have
• Meet with us links for calendar access though MS Bookings

```html
<!DOCTYPE html>
<html lang="en">
<head>
<meta charset="utf-8">
<title>Nexora Technology – Modern IT & Tech Service Solutions</title>
<link rel="stylesheet" href="https://fonts.googleapis.com/css2?family=Poppins:wght@400;500;600;700&family=Open+Sans:ital,wght@0,400;0,600;1,400&display=swap">
<style>
:root{
  --navy:#0f4a6e;
  --navy-deep:#0b3552;
  --ink:#1d2230;
  --footer:#1f2533;
  --footer-line:#2e3547;
  --yellow:#e4d160;
  --text:#6b7280;
  --light:#f4f5f7;
  --white:#ffffff;
  --red:#e0453a;
}
*{box-sizing:border-box;margin:0;padding:0}
html,body{width:1200px;height:4636px;overflow:hidden}
body{font-family:"Open Sans",Arial,sans-serif;color:var(--text);background:var(--white);font-size:13px;line-height:1.6}
.page{position:relative;width:1200px;height:4636px}
.abs{position:absolute}
h1,h2,h3,h4,.brand,.btn,.label{font-family:"Poppins",Arial,sans-serif}
h2{color:var(--ink);font-size:30px;line-height:1.25;font-weight:700}
h3{color:var(--ink);font-size:17px;font-weight:600}
.label{font-size:11px;font-weight:600;letter-spacing:1.5px;color:var(--ink);text-transform:uppercase}
.btn{display:inline-block;background:var(--yellow);color:var(--ink);font-size:11px;font-weight:600;letter-spacing:1px;padding:12px 24px;text-transform:uppercase}
.btn-outline{background:transparent;border:1px solid var(--yellow);color:var(--yellow)}
.more{font-family:"Poppins",Arial,sans-serif;font-size:10px;font-weight:600;letter-spacing:1px;color:#b9a83c;text-transform:uppercase}

/* hero */
.hero{left:0;top:0;width:1200px;height:580px;background:linear-gradient(100deg,#1c2735 0%,#3b4a59 45%,#7d8a93 100%)}
.hero-shade{left:0;top:0;width:1200px;height:580px;background:linear-gradient(90deg,rgba(10,18,28,.75),rgba(10,18,28,.15))}
.nav{left:160px;top:22px;width:880px;height:40px;display:flex;align-items:center;justify-content:space-between}
.brand{display:flex;align-items:center;gap:8px;color:var(--white);font-size:15px;font-weight:700;letter-spacing:.5px}
.brand i{width:14px;height:14px;border-radius:50%;background:var(--yellow);display:block}
.nav ul{display:flex;gap:34px;list-style:none;font-family:"Poppins",Arial,sans-serif;font-size:11px;font-weight:500;color:var(--white);letter-spacing:1px}
.nav ul li:first-child{color:var(--yellow)}
.nav .btn{padding:10px 20px}
.hero-title{left:160px;top:218px;width:520px;color:var(--white);font-size:46px;line-height:1.18;font-weight:700}
.hero-lead{left:160px;top:345px;width:430px;color:#e6e9ee;font-size:13px}
.hero-cta{left:160px;top:438px}

/* feature cards */
.feature{top:620px;height:220px;background:var(--white);box-shadow:0 10px 30px rgba(0,0,0,.08);padding:36px 28px;text-align:center}
.feature svg{margin-bottom:14px}
.feature h3{margin-bottom:10px}
.feature p{font-size:12px}
.feature-dark{background:var(--navy);text-align:center;padding-top:40px}
.feature-dark h3{color:var(--white);font-size:20px}
.feature-dark p{color:#cfdbe5}
.feature-dark .btn{margin-top:18px;padding:9px 22px}

/* about */
.about-visual{left:160px;top:925px;width:400px;height:400px;border-radius:50%;background:radial-gradient(circle at 50% 45%,#2d7bd0 0%,#123a78 45%,#061632 100%)}
.about-text{left:640px;top:930px;width:400px}
.about-text h2{margin:10px 0 18px}
.about-text p{margin-bottom:26px}
.ticks{list-style:none;margin-top:34px}
.ticks li{display:flex;gap:10px;align-items:center;margin-bottom:10px;font-size:12px}

/* services */
.services{left:0;top:1380px;width:1200px;height:630px;background:var(--light)}
.services-intro{left:160px;top:1450px;width:270px}
.services-intro h2{margin:10px 0 16px}
.services-intro p{margin-bottom:26px;font-size:12px}
.service{width:270px;height:230px;background:var(--white);padding:28px 30px;box-shadow:0 8px 24px rgba(0,0,0,.05)}
.service h3{margin:12px 0 10px}
.service p{font-size:12px;margin-bottom:16px}
.video{left:760px;top:1720px;width:280px;height:230px;background:linear-gradient(135deg,#c9b89f,#6d7a80 60%,#39434b)}
.play{left:880px;top:1815px}

/* testimonial */
.testi-photo{left:0;top:2040px;width:600px;height:350px;background:linear-gradient(120deg,#26333f,#4c6272 55%,#2a3742)}
.testi-panel{left:600px;top:2040px;width:600px;height:350px;background:var(--navy);text-align:center;padding:70px 60px 0}
.testi-panel h2{color:var(--white);font-size:28px}
.avatar{width:60px;height:60px;border-radius:50%;background:var(--white);margin:18px auto 16px}
.testi-panel blockquote{color:#e1e9f0;font-style:italic;font-size:13px;line-height:1.7}
.testi-panel cite{display:block;margin-top:16px;color:var(--white);font-style:normal;font-family:"Poppins",Arial,sans-serif;font-weight:600;font-size:13px}

/* case studies */
.cases-head{left:300px;top:2450px;width:600px;text-align:center}
.cases-head h2{margin:10px 0 14px}
.case{top:2730px;width:280px;height:300px;background:var(--white);box-shadow:0 8px 24px rgba(0,0,0,.06)}
.case-img{height:150px}
.case-bar{background:var(--navy);height:60px;padding:10px 18px}
.case-bar h4{color:var(--white);font-family:"Poppins",Arial,sans-serif;font-size:15px;font-weight:600;line-height:1.3}
.case-bar span{color:#bcd0de;font-size:11px}
.case-body{padding:14px 18px;font-size:12px}
.case-body .more{display:block;margin-top:12px}
.cases-note{left:300px;top:3058px;width:600px;text-align:center;font-size:12px}
.cases-note .more{margin-left:14px}

/* contact */
.contact-band{left:0;top:3160px;width:1200px;height:460px;background:linear-gradient(180deg,#151a21,#2b3139 60%,#1a1f26)}
.contact-head{left:260px;top:3250px;width:680px;text-align:center}
.contact-head h2{color:var(--white);font-size:32px}
.contact-head p{color:#c9ced5;margin-top:12px;font-size:12px}
.contact-box{left:160px;top:3440px;width:880px;height:550px;display:flex;box-shadow:0 20px 40px rgba(0,0,0,.12)}
.contact-info{width:420px;background:var(--navy);padding:50px 40px;color:#d3dee7}
.contact-info h3{color:var(--white);font-size:28px;line-height:1.25;font-weight:700;margin-bottom:18px}
.contact-info p{font-size:12px;margin-bottom:18px}
.contact-info .ticks{margin-top:0}
.contact-info .ticks li{color:#d3dee7}
.contact-actions{display:flex;gap:26px;align-items:center;margin-top:36px}
.contact-actions .btn-outline{color:var(--white);border-color:var(--white);padding:10px 20px}
.contact-actions .link{color:var(--white);font-family:"Poppins",Arial,sans-serif;font-size:11px;font-weight:600;letter-spacing:1px}
.contact-form{flex:1;background:var(--white);padding:46px 40px}
.field{margin-bottom:16px}
.field label{display:block;font-family:"Poppins",Arial,sans-serif;color:var(--ink);font-size:12px;font-weight:500;margin-bottom:6px}
.field div{height:34px;border:1px solid #dde1e6;padding:7px 12px;font-size:11px;color:#a1a7b0}
.field .area{height:110px}
.contact-form .btn{display:block;text-align:center;margin-top:8px}

/* trusted */
.trusted{left:300px;top:4040px;width:600px;text-align:center}
.trusted h3{font-size:22px;font-weight:700}
.partner{top:4150px;width:130px;height:36px;background:#c7cbd1;border-radius:3px}

/* footer */
.footer{left:0;top:4300px;width:1200px;height:336px;background:var(--footer);color:#a8afbd;font-size:12px}
.foot-col{top:4360px;color:#a8afbd;font-size:12px}
.foot-col h4{color:var(--white);font-family:"Poppins",Arial,sans-serif;font-size:14px;font-weight:600;margin-bottom:14px}
.foot-col ul{list-style:none}
.foot-col li{margin-bottom:6px}
.foot-col li::before{content:"› ";color:var(--yellow)}
.foot-brand .brand{margin-bottom:18px}
.foot-brand p{display:flex;gap:8px;align-items:center;margin-bottom:6px}
.subscribe{display:flex;margin-top:6px;width:260px}
.subscribe div{flex:1;height:34px;background:#fff;padding:8px 10px;font-size:11px;color:#9aa0aa}
.subscribe span{background:var(--navy);color:#fff;font-family:"Poppins",Arial,sans-serif;font-size:10px;font-weight:600;padding:10px 12px;letter-spacing:1px}
.social{display:flex;gap:10px;margin-top:20px}
.social i{width:30px;height:30px;background:#2f6fa8;display:block}
.foot-bottom{left:160px;top:4590px;width:880px;border-top:1px solid var(--footer-line);padding-top:14px;display:flex;justify-content:space-between;font-size:11px;color:#8990a0}
</style>
</head>
<body>
<div class="page">

  <!-- Hero -->
  <div class="abs hero" role="img" aria-label="Team of IT professionals working together at laptops in a bright office"></div>
  <div class="abs hero-shade"></div>
  <header class="abs nav">
    <div class="brand"><i></i>NEXORA TECHNOLOGY</div>
    <ul><li>HOME</li><li>ABOUT</li><li>SERVICES</li><li>PROJECTS</li><li>CONTACT</li></ul>
    <span class="btn">Get Started</span>
  </header>
  <h1 class="abs hero-title">Modern IT &amp; Tech Service Solutions</h1>
  <p class="abs hero-lead">We deliver dependable managed IT, cloud and security services so your business can run smoothly, stay protected and grow with confidence every day.</p>
  <span class="abs btn hero-cta">Contact Us</span>

  <!-- Feature cards -->
  <div class="abs feature" style="left:160px;width:220px">
    <svg width="34" height="34" viewBox="0 0 34 34" fill="none" stroke="#c9b43e" stroke-width="2"><circle cx="17" cy="13" r="8"/><path d="M13 22v6h8v-6"/></svg>
    <h3>IT Expertise</h3>
    <p>Certified engineers ready to plan, build and support your systems.</p>
  </div>
  <div class="abs feature" style="left:400px;width:220px">
    <svg width="34" height="34" viewBox="0 0 34 34" fill="none" stroke="#c9b43e" stroke-width="2"><circle cx="17" cy="17" r="12"/><path d="M17 10v7l5 3"/></svg>
    <h3>24/7 IT Support</h3>
    <p>Round-the-clock help desk keeping your team online at any hour.</p>
  </div>
  <div class="abs feature feature-dark" style="left:648px;width:392px">
    <h3>Custom Request</h3>
    <p>Need something specific? Tell us your goals and we will shape a tailored plan.</p>
    <span class="btn btn-outline">Find Out More</span>
  </div>

  <!-- About -->
  <div class="abs about-visual" role="img" aria-label="Hand touching a glowing digital security padlock interface"></div>
  <div class="abs about-text">
    <div class="label">About Us</div>
    <h2>Let Us Be Your Partners Preferred IT Partner</h2>
    <p>We work alongside your team to design, secure and maintain technology that fits the way you do business, with clear pricing and honest advice at every step of the journey.</p>
    <span class="btn">Get Started</span>
    <ul class="ticks">
      <li><svg width="14" height="14" viewBox="0 0 14 14"><path d="M2 7l3 3 7-7" fill="none" stroke="#c9b43e" stroke-width="2"/></svg>We are committed to providing quality IT Services</li>
      <li><svg width="14" height="14" viewBox="0 0 14 14"><path d="M2 7l3 3 7-7" fill="none" stroke="#c9b43e" stroke-width="2"/></svg>Provided by experts to help challenge critical activities</li>
      <li><svg width="14" height="14" viewBox="0 0 14 14"><path d="M2 7l3 3 7-7" fill="none" stroke="#c9b43e" stroke-width="2"/></svg>Really know the true needs and expectations of customers</li>
    </ul>
  </div>

  <!-- Services -->
  <div class="abs services"></div>
  <div class="abs services-intro">
    <div class="label">Our Services</div>
    <h2>Solutions &amp; Focus Areas</h2>
    <p>From daily support to long-term strategy, our services cover every layer of your technology stack.</p>
    <span class="btn">All Services</span>
  </div>
  <div class="abs service" style="left:460px;top:1460px">
    <svg width="30" height="30" viewBox="0 0 30 30" fill="none" stroke="#c9b43e" stroke-width="2"><rect x="4" y="6" width="22" height="15"/><path d="M10 25h10"/></svg>
    <h3>IT Management</h3>
    <p>Proactive monitoring and maintenance that keeps your systems healthy.</p>
    <span class="more">Read More ›</span>
  </div>
  <div class="abs service" style="left:760px;top:1460px">
    <svg width="30" height="30" viewBox="0 0 30 30" fill="none" stroke="#c9b43e" stroke-width="2"><path d="M15 3l10 4v7c0 6-4 10-10 13C9 24 5 20 5 14V7z"/></svg>
    <h3>Cyber Security</h3>
    <p>Layered protection for your data, devices and people against threats.</p>
    <span class="more">Read More ›</span>
  </div>
  <div class="abs service" style="left:160px;top:1720px">
    <svg width="30" height="30" viewBox="0 0 30 30" fill="none" stroke="#c9b43e" stroke-width="2"><path d="M8 22h15a5 5 0 000-10 7 7 0 00-13-2A6 6 0 008 22z"/></svg>
    <h3>Cloud Computing</h3>
    <p>Flexible cloud platforms that scale with your business and budget.</p>
    <span class="more">Read More ›</span>
  </div>
  <div class="abs service" style="left:460px;top:1720px">
    <svg width="30" height="30" viewBox="0 0 30 30" fill="none" stroke="#c9b43e" stroke-width="2"><path d="M10 9l-6 6 6 6M20 9l6 6-6 6"/></svg>
    <h3>Software Developer</h3>
    <p>Custom applications built around your workflows and your customers.</p>
    <span class="more">Read More ›</span>
  </div>
  <div class="abs video" role="img" aria-label="Colleagues collaborating around a laptop in a meeting room"></div>
  <svg class="abs play" width="40" height="40" viewBox="0 0 40 40"><circle cx="20" cy="20" r="20" fill="#e0453a"/><path d="M16 12l12 8-12 8z" fill="#fff"/></svg>

  <!-- Testimonial -->
  <div class="abs testi-photo" role="img" aria-label="Presenter explaining charts on a screen to a business team"></div>
  <div class="abs testi-panel">
    <h2>What Client Say About Us</h2>
    <div class="avatar" role="img" aria-label="Client portrait"></div>
    <blockquote>“Their team answered every call fast and moved our whole office to the cloud without a single day lost. We finally have IT we never need to worry about.”</blockquote>
    <cite>Marlon Avery</cite>
  </div>

  <!-- Case studies -->
  <div class="abs cases-head">
    <div class="label">Case Studies</div>
    <h2>IT Solutions &amp; Projects</h2>
    <p>A look at recent projects where we helped clients modernise operations and protect their data.</p>
  </div>
  <div class="abs case" style="left:160px">
    <div class="case-img" style="background:linear-gradient(135deg,#2f3f4f,#7a8894)" role="img" aria-label="Team reviewing workflow plans at a desk"></div>
    <div class="case-bar"><h4>Workflow Management</h4><span>IT Management</span></div>
    <div class="case-body">Streamlined daily operations with automated tools and clear reporting.<span class="more">View Details ›</span></div>
  </div>
  <div class="abs case" style="left:460px">
    <div class="case-img" style="background:linear-gradient(135deg,#d9dde2,#8b98a6)" role="img" aria-label="Hands working on documents and a laptop"></div>
    <div class="case-bar"><h4>IT Practices In Cloud</h4><span>Cloud Computing</span></div>
    <div class="case-body">Moved core systems to a secure cloud with zero unplanned downtime.<span class="more">View Details ›</span></div>
  </div>
  <div class="abs case" style="left:760px">
    <div class="case-img" style="background:linear-gradient(135deg,#3b4c5a,#9aa7a0)" role="img" aria-label="Developer writing code on multiple monitors"></div>
    <div class="case-bar"><h4>Software For Financial</h4><span>Software Developer</span></div>
    <div class="case-body">Built a reliable reporting platform for a growing finance team.<span class="more">View Details ›</span></div>
  </div>
  <p class="abs cases-note">Nothing start to your customize here? <span class="more">Get Started ›</span></p>

  <!-- Contact -->
  <div class="abs contact-band" role="img" aria-label="Close-up of a dark keyboard"></div>
  <div class="abs contact-head">
    <h2>Don’t Hesitate To Contact Us For Better Information And Services</h2>
    <p>Reach out today and our specialists will get back to you within one business day.</p>
  </div>
  <div class="abs contact-box">
    <div class="contact-info">
      <h3>Perfect Solutions For Your Business</h3>
      <p>Whether you need a quick fix or a long-term partner, we shape our services around your goals and your budget.</p>
      <ul class="ticks">
        <li><svg width="14" height="14" viewBox="0 0 14 14"><path d="M2 7l3 3 7-7" fill="none" stroke="#e4d160" stroke-width="2"/></svg>We are committed to providing quality IT Services</li>
        <li><svg width="14" height="14" viewBox="0 0 14 14"><path d="M2 7l3 3 7-7" fill="none" stroke="#e4d160" stroke-width="2"/></svg>Provided by experts to help challenge critical activities</li>
        <li><svg width="14" height="14" viewBox="0 0 14 14"><path d="M2 7l3 3 7-7" fill="none" stroke="#e4d160" stroke-width="2"/></svg>Really know the true needs and expectations of customers</li>
        <li><svg width="14" height="14" viewBox="0 0 14 14"><path d="M2 7l3 3 7-7" fill="none" stroke="#e4d160" stroke-width="2"/></svg>Processes of achieving the excellent improvements</li>
      </ul>
      <div class="contact-actions"><span class="btn btn-outline">Meet With Us</span><span class="link">GET STARTED →</span></div>
    </div>
    <div class="contact-form">
      <div class="field"><label>Name</label><div>Name</div></div>
      <div class="field"><label>Phone</label><div>Phone</div></div>
      <div class="field"><label>Email</label><div>Email</div></div>
      <div class="field"><label>Message</label><div class="area">Message</div></div>
      <span class="btn">Send</span>
    </div>
  </div>

  <!-- Trusted -->
  <div class="abs trusted"><h3>Trusted By The World’s Best Organizations</h3></div>
  <div class="abs partner" style="left:200px"></div>
  <div class="abs partner" style="left:410px"></div>
  <div class="abs partner" style="left:660px"></div>
  <div class="abs partner" style="left:870px"></div>

  <!-- Footer -->
  <div class="abs footer"></div>
  <div class="abs foot-col foot-brand" style="left:160px;width:300px">
    <div class="brand"><i></i>NEXORA TECHNOLOGY</div>
    <p><svg width="12" height="12" viewBox="0 0 12 12"><path d="M6 1a4 4 0 014 4c0 3-4 6-4 6S2 8 2 5a4 4 0 014-4z" fill="#e4d160"/></svg>48 Harbor Lane, Suite 210, Brookfield</p>
    <p><svg width="12" height="12" viewBox="0 0 12 12"><rect x="1" y="2" width="10" height="8" fill="none" stroke="#e4d160"/></svg>hello@nexoratech.io</p>
    <p><svg width="12" height="12" viewBox="0 0 12 12"><path d="M2 1h3l1 3-2 1a7 7 0 003 3l1-2 3 1v3c-6 0-9-3-9-9z" fill="#e4d160"/></svg>(555) 014-2297</p>
  </div>
  <div class="abs foot-col" style="left:460px">
    <h4>Other Pages</h4>
    <ul><li>Home</li><li>About Us</li><li>Services</li><li>Contact</li><li>Project</li></ul>
  </div>
  <div class="abs foot-col" style="left:610px">
    <h4>Quick Links</h4>
    <ul><li>Privacy Policy</li><li>Term Of Service</li><li>Disclaimer</li><li>Credits</li><li>FAQ</li></ul>
  </div>
  <div class="abs foot-col" style="left:780px;width:260px">
    <h4>Newsletter</h4>
    <div class="subscribe"><div>Email address</div><span>SUBSCRIBE</span></div>
    <div class="social"><i></i><i></i><i></i><i></i></div>
  </div>
  <div class="abs foot-bottom"><span>Technology &amp; IT Solution</span><span>Copyright © 2024 All rights reserved.</span></div>

</div>
</body>
</html>
```